New business card for a regional office of a US M&A company

We need business card for a finance company, office based in Hong Kong , our Head office is in US, our business is to Merge and acquires companies , the new office will be a regional office for the Asia Pacific region. We want to use the head office logo as attached ( but don't have to be exactly the same, can be a variation to it) as a base and then add Asia Pacific alongside the logo.
We would prefer to have be bilingual Eng + Chinese, although we don't really have Chinese company name .

Industry/Entity Type

Business

Contact Information for Business Card

Carla Beth Soren
 

VP,
APAC M&A Operations
Tovar Crest Asia Pacific Limited
 
Unit 1407, K82
27 Sai Lok Fung Road, 
Hong Kong 
 
M: +852 6481 2037
T : +852 2736 4100
F : +852 2736 4155
VOIP: 4813
 
cbsoren@tovarcrest.com

Font styles to use
Serif
Sans Serif

Colors

Designer to choose colors to be used in the design.

Requirements
Must have
• APAC Office

```html
<!DOCTYPE html>
<html lang="en">
<head>
<meta charset="utf-8">
<title>Tovar Crest Asia Pacific – Business Card</title>
<link rel="stylesheet" href="https://fonts.googleapis.com/css2?family=Open+Sans:wght@700&family=Roboto:wght@400&family=Roboto+Condensed:wght@700&display=swap">
<style>
  :root {
    --backdrop: #e8e5e0;
    --navy: #0f2a45;
    --sky: #1eaed3;
    --brand-blue: #20a8d6;
    --ink-light: #e4ecf3;
    --rule: #8fa3b8;
    --white: #ffffff;
  }
  * { margin: 0; padding: 0; box-sizing: border-box; }
  html, body {
    width: 1200px; height: 960px; overflow: hidden;
    background: var(--backdrop);
  }
  .canvas { position: relative; width: 1200px; height: 960px; }

  .card {
    position: absolute; width: 600px; height: 342px;
    box-shadow: 0 3px 6px rgba(0,0,0,0.35);
  }

  /* Front */
  .card-front { left: 314px; top: 113px; background: var(--navy); }
  .name-tab {
    position: absolute; left: 0; top: 119px; width: 13px; height: 38px;
    background: var(--white);
  }
  .holder-name {
    position: absolute; left: 34px; top: 116px;
    font: 700 21px/1 "Roboto Condensed", sans-serif;
    color: var(--brand-blue); text-transform: uppercase;
  }
  .holder-title {
    position: absolute; left: 36px; top: 144px;
    font: 400 15px/1 "Roboto", sans-serif; color: var(--white);
  }
  .divider {
    position: absolute; left: 34px; top: 163px; width: 529px; height: 1px;
    background: var(--rule);
  }
  .brand {
    position: absolute; right: 37px; top: 32px;
    display: flex; flex-direction: column; align-items: flex-end; gap: 14px;
  }
  .brand-square { width: 40px; height: 40px; background: var(--white); }
  .brand-name {
    font: 700 38px/1 "Open Sans", sans-serif;
    color: var(--brand-blue); letter-spacing: 0.5px;
  }
  .contacts {
    position: absolute; left: 36px; top: 230px; list-style: none;
    font: 400 14.5px/19px "Roboto", sans-serif; color: var(--ink-light);
  }
  .contacts li { display: flex; align-items: center; gap: 8px; }
  .contacts svg { width: 13px; height: 13px; fill: var(--brand-blue); }
  .voip {
    position: absolute; left: 35px; top: 295px;
    font: 400 14.5px/1 "Roboto", sans-serif; color: var(--ink-light);
  }
  .address {
    position: absolute; right: 38px; top: 225px; text-align: right;
    font: 400 14.5px/19px "Roboto", sans-serif; color: var(--ink-light);
    font-style: normal;
  }

  /* Back */
  .card-back { left: 311px; top: 472px; background: var(--sky); }
  .back-brand {
    position: absolute; left: 0; right: 0; top: 78px;
    display: flex; flex-direction: column; align-items: center; gap: 26px;
  }
  .back-square { width: 110px; height: 110px; background: var(--navy); }
  .back-name {
    font: 700 36px/1 "Open Sans", sans-serif; color: var(--navy);
  }
  .website {
    position: absolute; left: 0; right: 0; top: 286px; text-align: center;
    font: 400 14px/1 "Roboto", sans-serif; color: var(--navy);
    letter-spacing: 7px;
  }
</style>
</head>
<body>
<main class="canvas">
  <section class="card card-front">
    <div class="name-tab"></div>
    <h1 class="holder-name">Carla Beth Soren</h1>
    <p class="holder-title">VP</p>
    <div class="divider"></div>

    <div class="brand">
      <div class="brand-square"></div>
      <div class="brand-name">TOVAR CREST</div>
    </div>

    <ul class="contacts">
      <li>
        <svg viewBox="0 0 16 16" aria-label="Telephone"><path d="M3.6 1.2l2.3 2.7-1.3 2c.9 2 2.6 3.7 4.5 4.6l2-1.3 2.7 2.3-1.3 2.5C7.6 14 2 8.4 1.1 2.5z"/></svg>
        <span>+852 2736 4100</span>
      </li>
      <li>
        <svg viewBox="0 0 16 16" aria-label="Mobile"><path d="M4.5 0h7a1 1 0 0 1 1 1v14a1 1 0 0 1-1 1h-7a1 1 0 0 1-1-1V1a1 1 0 0 1 1-1zm.5 2v10h6V2zm3 11a1 1 0 1 0 0 2 1 1 0 0 0 0-2z"/></svg>
        <span>+852 6481 2037</span>
      </li>
      <li>
        <svg viewBox="0 0 16 16" aria-label="Fax"><path d="M4 1h8v4H4zM1 6h14v6h-2v3H3v-3H1zm4 5v3h6v-3z"/></svg>
        <span>+852 2736 4155</span>
      </li>
    </ul>
    <p class="voip">VOIP: 4813</p>

    <address class="address">
      APAC M&amp;A Operations<br>
      Tovar Crest Asia Pacific Limited<br>
      Unit 1407, K82<br>
      27 Sai Lok Fung Road<br>
      Hong Kong
    </address>
  </section>

  <section class="card card-back">
    <div class="back-brand">
      <div class="back-square"></div>
      <div class="back-name">TOVAR CREST</div>
    </div>
    <p class="website">www.tovarcrest.com</p>
  </section>
</main>
</body>
</html>
```